SEAFOOD PACKAGING (Products for consumer)

We are looking to create packaging for various seafood products such as octopus and squid. We plan to sell our products in upscale supermarkets.

We are specializing in cut octopus this time.

Please include our company logo. Also, please leave a transparent area so that customers can see the product inside.
Updates

We want to show what is inside, so a picture of the octopus is not required. We need something simple and sophisticated.

Target Market(s)

upscale store in US and ASIA

Industry/Entity Type

Fisheries dealer

Requirements
Must have
• Please include the attached logo,Blue one is preferred.Please leave a transparent part so that the contents of the product can be seen by the consumer.1. product name on packaging →CUT OCTOPUS,TAKO SASHIMI,Highest quality,Top quality etc... 3. What text information should be on the packaging →(It may be edited, but this is the image) The raw materials are caught in a very clean environment and processed in a modern factory with ZEK certification. We are committed to additive-free products. 4. Packing size(cm/inch)→it will be about 19cm*22cm. 5. what kind of packaging do you use →PP or PA 6. dll →ai,jag
Nice to have
• https://quillmora.example/shots/4829174-Velka-Reef We need something simple and sophisticated like this one.
Should not have
• We want to show what is inside, so a picture of the octopus is not required. We need something simple and sophisticated.

```html
<!DOCTYPE html>
<html lang="en">
<head>
<meta charset="utf-8">
<title>Marelo Seafood Packaging</title>
<link rel="stylesheet" href="https://fonts.googleapis.com/css2?family=Poppins:wght@300;400;600;700&display=swap">
<style>
  :root {
    --stage: #ececec;
    --white: #ffffff;
    --deep-blue: #1d5fd8;
    --deep-blue-dark: #1a52c4;
    --deep-blue-light: #2a6ee2;
    --sky-blue: #17b6ee;
    --sky-blue-dark: #12a4e0;
    --sky-blue-light: #3cc4f3;
    --ink-blue: #1f56c9;
    --lavender: #a9b6ee;
    --octopus-tone-a: #eef0f0;
    --octopus-tone-b: #c9cfd3;
    --squid-tone-a: #e9d7da;
    --squid-tone-b: #b77a89;
  }
  * { margin: 0; padding: 0; box-sizing: border-box; }
  html, body { width: 1200px; height: 675px; overflow: hidden; }
  body {
    background: var(--stage);
    font-family: "Poppins", Arial, sans-serif;
    position: relative;
  }
  .pack {
    position: absolute;
    top: 45px;
    width: 487px;
    height: 560px;
    overflow: hidden;
    background: var(--pack-main);
  }
  .pack--octopus {
    left: 90px;
    --pack-main: var(--deep-blue); --pack-main-dark: var(--deep-blue-dark); --pack-main-light: var(--deep-blue-light);
    --pack-accent: var(--sky-blue); --pack-accent-dark: var(--sky-blue-dark); --pack-accent-light: var(--sky-blue-light);
    --window-a: var(--octopus-tone-a); --window-b: var(--octopus-tone-b);
  }
  .pack--squid {
    left: 592px;
    --pack-main: var(--sky-blue); --pack-main-dark: var(--sky-blue-dark); --pack-main-light: var(--sky-blue-light);
    --pack-accent: var(--deep-blue); --pack-accent-dark: var(--deep-blue-dark); --pack-accent-light: var(--deep-blue-light);
    --window-a: var(--squid-tone-a); --window-b: var(--squid-tone-b);
  }

  .side-pattern {
    position: absolute; top: 0; width: 145px; height: 560px;
    background: linear-gradient(160deg, var(--pack-main-light), var(--pack-main) 45%, var(--pack-main-dark));
  }
  .side-pattern--left { left: 0; }
  .side-pattern--right { left: 337px; width: 150px; }

  .brand-panel {
    position: absolute; left: 145px; top: 0; width: 192px; height: 190px;
    background: var(--white); color: var(--ink-blue); text-align: center;
  }
  .brand-name {
    position: absolute; left: 0; right: 0; top: 45px;
    display: flex; align-items: center; justify-content: center; gap: 8px;
    font-weight: 600; font-size: 28px; letter-spacing: 3px; line-height: 32px;
  }
  .brand-dot { width: 18px; height: 18px; border-radius: 50%; background: var(--ink-blue); }
  .tagline-top {
    position: absolute; left: 0; right: 0; top: 99px;
    font-weight: 300; font-size: 16.5px; line-height: 22px;
  }
  .tagline-main {
    position: absolute; left: 0; right: 0; top: 115px;
    font-weight: 400; font-size: 32px; line-height: 40px; letter-spacing: 0.5px;
  }
  .tagline-sub {
    position: absolute; left: 30px; width: 132px; top: 157px; height: 26px;
    border-top: 1px solid var(--sky-blue); border-bottom: 1px solid var(--sky-blue);
    font-weight: 300; font-size: 12.5px; line-height: 24px; color: var(--sky-blue); white-space: nowrap;
  }

  .name-panel {
    position: absolute; left: 145px; top: 190px; width: 192px; height: 150px;
    background: var(--pack-accent); color: var(--white); text-align: center;
  }
  .product-name {
    position: absolute; left: 0; right: 0; top: 16px;
    font-weight: 700; font-size: 42px; letter-spacing: -1px; line-height: 50px;
  }
  .product-cut {
    position: absolute; left: 0; right: 0; top: 65px;
    font-weight: 300; font-size: 21px; line-height: 28px;
  }

  .product-window {
    position: absolute; left: 28px; top: 316px; width: 430px; height: 142px;
    background: linear-gradient(135deg, var(--window-a), var(--window-b) 55%, var(--window-a));
    border-radius: 4px;
  }
  .wave-band { position: absolute; left: 0; top: 290px; width: 487px; height: 80px; }

  .seal { position: absolute; display: block; }
  .seal--natural { left: 49px; top: 81px; width: 90px; height: 90px; }
  .seal--quality { left: 293px; top: 269px; width: 84px; height: 84px; }
  .seal-text { font-family: "Poppins", Arial, sans-serif; font-weight: 600; fill: var(--white); }

  .footer-stripe {
    position: absolute; left: 145px; top: 458px; width: 192px; height: 102px;
    background: linear-gradient(180deg, var(--pack-accent-light), var(--pack-accent) 50%, var(--pack-accent-dark));
  }

  .claims { position: absolute; left: 45px; top: 476px; list-style: none; }
  .claim {
    display: flex; align-items: center; gap: 5px; width: 82px; height: 12px; margin-bottom: 3px;
    border-radius: 6px; color: var(--white); background: var(--claim-bg);
    font-size: 6.5px; line-height: 12px; font-weight: 400; white-space: nowrap;
  }
  .pack--octopus .claim { --claim-bg: var(--sky-blue); }
  .pack--squid .claim { --claim-bg: var(--deep-blue); }
  .claim-tick {
    width: 20px; height: 12px; border-radius: 6px; background: var(--white);
    display: flex; align-items: center; justify-content: center;
  }

  .net-weight {
    position: absolute; right: 50px; top: 492px; text-align: right;
    color: var(--white); font-size: 9.5px; line-height: 1.3; font-weight: 300;
  }
  .net-weight strong { font-weight: 600; }
</style>
</head>
<body>

<section class="pack pack--octopus">
  <div class="side-pattern side-pattern--left" role="img" aria-label="Faint repeating nautical pattern in tonal blue"></div>
  <div class="side-pattern side-pattern--right" role="img" aria-label="Faint repeating nautical pattern in tonal blue"></div>
  <div class="product-window" role="img" aria-label="Clear window showing cut white octopus tentacles inside the bag"></div>
  <svg class="wave-band" viewBox="0 0 487 80" aria-hidden="true">
    <path d="M0 40 C120 18 260 10 487 28 L487 44 C300 28 160 40 0 64 Z" fill="var(--sky-blue)"/>
    <path d="M60 50 C180 30 280 20 340 22 L340 30 C260 32 160 48 60 62 Z" fill="var(--deep-blue)"/>
  </svg>
  <div class="brand-panel">
    <div class="brand-name"><span class="brand-dot"></span>MARELO</div>
    <p class="tagline-top">PREMIUM QUALITY</p>
    <p class="tagline-main">SEAFOOD</p>
    <p class="tagline-sub">HAND PICKED &amp; SORTED</p>
  </div>
  <div class="name-panel">
    <h1 class="product-name">Octopus</h1>
    <p class="product-cut">PRIME CUTS</p>
  </div>
  <svg class="seal seal--natural" viewBox="0 0 90 90" aria-label="100% natural">
    <defs>
      <path id="oct-nat-top" d="M16 45 A29 29 0 0 1 74 45"/>
      <path id="oct-nat-bot" d="M16 45 A29 29 0 0 0 74 45"/>
    </defs>
    <circle cx="45" cy="45" r="43" fill="var(--white)"/>
    <circle cx="45" cy="45" r="29" fill="none" stroke="var(--sky-blue)" stroke-width="14"/>
    <circle cx="45" cy="45" r="22" fill="var(--lavender)"/>
    <text class="seal-text" font-size="8.5" letter-spacing="1.5"><textPath href="#oct-nat-top" startOffset="50%" text-anchor="middle" dominant-baseline="middle">NATURAL</textPath></text>
    <text class="seal-text" font-size="8.5" letter-spacing="1.5"><textPath href="#oct-nat-bot" startOffset="50%" text-anchor="middle" dominant-baseline="middle">NATURAL</textPath></text>
    <polygon points="1,36 89,36 86,45 89,54 1,54 4,45" fill="var(--deep-blue)" stroke="var(--white)" stroke-width="1.5"/>
    <text class="seal-text" x="45" y="50.5" font-size="15" font-weight="700" text-anchor="middle">100%</text>
  </svg>
  <svg class="seal seal--quality" viewBox="0 0 84 84" aria-label="Quality guaranteed">
    <defs>
      <path id="oct-q-top" d="M14 42 A28 28 0 0 1 70 42"/>
      <path id="oct-q-bot" d="M14 42 A28 28 0 0 0 70 42"/>
    </defs>
    <circle cx="42" cy="42" r="41" fill="var(--white)"/>
    <circle cx="42" cy="42" r="37.5" fill="var(--sky-blue)"/>
    <text class="seal-text" font-size="8" letter-spacing="2"><textPath href="#oct-q-top" startOffset="50%" text-anchor="middle" dominant-baseline="middle">QUALITY</textPath></text>
    <text class="seal-text" font-size="8" letter-spacing="1.5"><textPath href="#oct-q-bot" startOffset="50%" text-anchor="middle" dominant-baseline="middle">GUARANTEED</textPath></text>
    <circle cx="15" cy="42" r="1.6" fill="var(--white)"/>
    <circle cx="69" cy="42" r="1.6" fill="var(--white)"/>
    <circle cx="42" cy="42" r="20" fill="var(--white)"/>
    <circle cx="42" cy="42" r="17.5" fill="var(--deep-blue)"/>
  </svg>
  <div class="footer-stripe" role="img" aria-label="Fine wavy line texture in light blue"></div>
  <ul class="claims">
    <li class="claim"><span class="claim-tick"><svg width="10" height="7" viewBox="0 0 10 7"><path d="M1 3.5 L4 6 L9 1" stroke="var(--ink-blue)" stroke-width="1.6" fill="none"/></svg></span>No preservatives</li>
    <li class="claim"><span class="claim-tick"><svg width="10" height="7" viewBox="0 0 10 7"><path d="M1 3.5 L4 6 L9 1" stroke="var(--ink-blue)" stroke-width="1.6" fill="none"/></svg></span>Keep frozen</li>
    <li class="claim"><span class="claim-tick"><svg width="10" height="7" viewBox="0 0 10 7"><path d="M1 3.5 L4 6 L9 1" stroke="var(--ink-blue)" stroke-width="1.6" fill="none"/></svg></span>ZEK Certified</li>
  </ul>
  <p class="net-weight">NET WT<br><strong>1 LB (454g)</strong></p>
</section>

<section class="pack pack--squid">
  <div class="side-pattern side-pattern--left" role="img" aria-label="Faint repeating nautical pattern in tonal light blue"></div>
  <div class="side-pattern side-pattern--right" role="img" aria-label="Faint repeating nautical pattern in tonal light blue"></div>
  <div class="product-window" role="img" aria-label="Clear window showing whole pink and white squid inside the bag"></div>
  <svg class="wave-band" viewBox="0 0 487 80" aria-hidden="true">
    <path d="M0 40 C120 18 260 10 487 28 L487 44 C300 28 160 40 0 64 Z" fill="var(--deep-blue)"/>
    <path d="M60 50 C180 30 280 20 340 22 L340 30 C260 32 160 48 60 62 Z" fill="var(--sky-blue)"/>
  </svg>
  <div class="brand-panel">
    <div class="brand-name"><span class="brand-dot"></span>MARELO</div>
    <p class="tagline-top">PREMIUM QUALITY</p>
    <p class="tagline-main">SEAFOOD</p>
    <p class="tagline-sub">SOURCED FROM ASIA</p>
  </div>
  <div class="name-panel">
    <h1 class="product-name">Squid</h1>
    <p class="product-cut">MEAT</p>
  </div>
  <svg class="seal seal--natural" viewBox="0 0 90 90" aria-label="100% natural">
    <defs>
      <path id="sq-nat-top" d="M16 45 A29 29 0 0 1 74 45"/>
      <path id="sq-nat-bot" d="M16 45 A29 29 0 0 0 74 45"/>
    </defs>
    <circle cx="45" cy="45" r="43" fill="var(--white)"/>
    <circle cx="45" cy="45" r="29" fill="none" stroke="var(--deep-blue)" stroke-width="14"/>
    <circle cx="45" cy="45" r="22" fill="var(--lavender)"/>
    <text class="seal-text" font-size="8.5" letter-spacing="1.5"><textPath href="#sq-nat-top" startOffset="50%" text-anchor="middle" dominant-baseline="middle">NATURAL</textPath></text>
    <text class="seal-text" font-size="8.5" letter-spacing="1.5"><textPath href="#sq-nat-bot" startOffset="50%" text-anchor="middle" dominant-baseline="middle">NATURAL</textPath></text>
    <polygon points="1,36 89,36 86,45 89,54 1,54 4,45" fill="var(--sky-blue)" stroke="var(--deep-blue)" stroke-width="1.5"/>
    <text class="seal-text" x="45" y="50.5" font-size="15" font-weight="700" text-anchor="middle">100%</text>
  </svg>
  <svg class="seal seal--quality" viewBox="0 0 84 84" aria-label="Top quality guaranteed">
    <defs>
      <path id="sq-q-top" d="M14 42 A28 28 0 0 1 70 42"/>
      <path id="sq-q-bot" d="M14 42 A28 28 0 0 0 70 42"/>
    </defs>
    <circle cx="42" cy="42" r="41" fill="var(--white)"/>
    <circle cx="42" cy="42" r="37.5" fill="var(--deep-blue)"/>
    <text class="seal-text" font-size="8" letter-spacing="1.5"><textPath href="#sq-q-top" startOffset="50%" text-anchor="middle" dominant-baseline="middle">TOP QUALITY</textPath></text>
    <text class="seal-text" font-size="8" letter-spacing="1.5"><textPath href="#sq-q-bot" startOffset="50%" text-anchor="middle" dominant-baseline="middle">GUARANTEED</textPath></text>
    <circle cx="15" cy="42" r="1.6" fill="var(--white)"/>
    <circle cx="69" cy="42" r="1.6" fill="var(--white)"/>
    <circle cx="42" cy="42" r="20" fill="var(--white)"/>
    <circle cx="42" cy="42" r="17.5" fill="var(--sky-blue)"/>
  </svg>
  <div class="footer-stripe" role="img" aria-label="Fine wavy line texture in deep blue"></div>
  <ul class="claims">
    <li class="claim"><span class="claim-tick"><svg width="10" height="7" viewBox="0 0 10 7"><path d="M1 3.5 L4 6 L9 1" stroke="var(--ink-blue)" stroke-width="1.6" fill="none"/></svg></span>No preservatives</li>
    <li class="claim"><span class="claim-tick"><svg width="10" height="7" viewBox="0 0 10 7"><path d="M1 3.5 L4 6 L9 1" stroke="var(--ink-blue)" stroke-width="1.6" fill="none"/></svg></span>Keep frozen</li>
    <li class="claim"><span class="claim-tick"><svg width="10" height="7" viewBox="0 0 10 7"><path d="M1 3.5 L4 6 L9 1" stroke="var(--ink-blue)" stroke-width="1.6" fill="none"/></svg></span>ZEK Certified</li>
  </ul>
  <p class="net-weight">NET WT<br><strong>1 LB (454g)</strong></p>
</section>

</body>
</html>
```